Modern logo for digital marketing consulting company
Modern, expensive, innovative, related
Modern logo for digital marketing consulting company - Consulting
Creative Brief
Professional
Tomas Belruškevičius
Digital Marketing Consultant
Not needed
tomas@brightmetrika.lt
www.brightmetrika.lt
Card should represent company values: modern, innovative, quality = experience. The most important information on a card is: logo, person name, title, URL. Optional: phone and email address. Design may be brave and non standard, showing that company is not afraid of innovative solutions. It would be best if design is related to company activity. For example one idea: design main object is a Pixeltrend Insights graph with improving results. At the point where result is about to improve, we see an annotation "Hired Tomas" or "Hired consultant".
Must include: QR code with business card details (attached). May include: logotype or logotype icon (attached)

```html
<!DOCTYPE html>
<html lang="en">
<head>
<meta charset="UTF-8">
<title>brightmetrika – business card</title>
<link rel="stylesheet" href="https://fonts.googleapis.com/css2?family=Open+Sans:wght@300;400;600&display=swap">
<style>
  :root {
    --backdrop: #d9d9d9;
    --card: #ffffff;
    --accent: #1fa3d6;
    --ink: #4a4a4a;
    --ink-soft: #6e6e6e;
    --qr-fill: #e4e4e4;
    --qr-edge: #c9c9c9;
  }
  * { margin: 0; padding: 0; box-sizing: border-box; }
  html, body { width: 1200px; height: 902px; overflow: hidden; }
  body {
    background: var(--backdrop);
    font-family: "Open Sans", Arial, sans-serif;
    position: relative;
  }
  .card {
    position: absolute;
    width: 580px;
    height: 331px;
    background: var(--card);
    box-shadow: 0 4px 14px rgba(0,0,0,0.18);
  }
  .card--back { left: 310px; top: 90px; }
  .card--front { left: 310px; top: 481px; }

  .contact {
    position: absolute;
    right: 34px;
    top: 34px;
    text-align right;
    text-align: right;
    font-size: 12px;
    line-height: 19px;
    color: var(--ink-soft);
  }
  .contact__email { display: flex; align-items: center; justify-content: flex-end; gap: 6px; }
  .contact__email svg { width: 11px; height: 9px; }
  .qr-code {
    position: absolute;
    right: 34px;
    bottom: 30px;
    width: 80px;
    height: 80px;
    background: var(--qr-fill);
    border: 1px solid var(--qr-edge);
  }
  .website {
    position: absolute;
    left: 34px;
    bottom: 30px;
    font-size: 15px;
    letter-spacing: 2px;
    color: var(--accent);
  }

  .brand {
    position: absolute;
    left: 34px;
    bottom: 30px;
    display: flex;
    align-items: center;
    gap: 10px;
  }
  .brand__mark { width: 26px; height: 26px; background: var(--ink); }
  .brand__name {
    font-size: 34px;
    font-weight: 300;
    letter-spacing: -0.5px;
    color: var(--accent);
  }
  .person {
    position: absolute;
    right: 34px;
    top: 112px;
    text-align: right;
  }
  .person__name { font-size: 17px; font-weight: 600; color: var(--accent); white-space: nowrap; }
  .person__title { font-size: 13px; color: var(--ink-soft); margin-top: 2px; white-space: nowrap; }
</style>
</head>
<body>
  <section class="card card--back" aria-label="Card back">
    <div class="contact">
      <p>24 Linden Row</p>
      <p>Vilnius LT 01105</p>
      <p>555.010.4420</p>
      <p class="contact__email">tomas@brightmetrika.lt
        <svg viewBox="0 0 11 9" aria-hidden="true"><rect width="11" height="9" fill="#1fa3d6"/><path d="M0 0 L5.5 5 L11 0" fill="none" stroke="#fff" stroke-width="1"/></svg>
      </p>
    </div>
    <div class="qr-code" role="img" aria-label="QR code with business card details"></div>
    <p class="website">www.brightmetrika.lt</p>
  </section>

  <section class="card card--front" aria-label="Card front">
    <div class="brand">
      <span class="brand__mark"></span>
      <span class="brand__name">brightmetrika</span>
    </div>
    <div class="person">
      <p class="person__name">Tomas Belruškevičius</p>
      <p class="person__title">Digital Marketing Consultant</p>
    </div>
  </section>
</body>
</html>
```